Corvelle BSH Book Cover Design: Book 1 of 4

Designers must not submit more than 1 design. Submission of multiple designs will result in disqualification.

Designer must be highly experienced with properly designing and formatting Corvelle BSH book covers. The winner of this contest will receive three more covers to do. This project is for one of four books in a series. I want the same designer to do all four books because they are in a series and need to look the same. Attached are the directions and files.

Target Market(s)

see attachments

Industry/Entity Type

see attachments

Requirements
Must have
• see attachments
Nice to have
• see attachments
Should not have
• see attachments

```html
<!DOCTYPE html>
<html lang="en">
<head>
<meta charset="utf-8">
<title>Before You Pay — Full Wrap Cover</title>
<link rel="stylesheet" href="https://fonts.googleapis.com/css2?family=Archivo+Black&family=Oswald:wght@500;600;700&family=Source+Sans+3:ital,wght@0,400;0,600;1,400&display=swap">
<style>
  :root {
    --navy: #0d1c33;
    --navy-deep: #0a1628;
    --ink: #13233f;
    --orange: #e08a1e;
    --orange-strong: #c9650c;
    --orange-soft: #d98a2a;
    --white: #ffffff;
    --cream: #f3ebdf;
  }
  * { box-sizing: border-box; margin: 0; padding: 0; }
  html, body { width: 1200px; height: 800px; overflow: hidden; background: var(--navy-deep); }
  .cover { position: relative; width: 1200px; height: 800px; background: var(--navy); color: var(--white); font-family: "Source Sans 3", Arial, sans-serif; }

  /* ---------- back cover ---------- */
  .back { position: absolute; left: 0; top: 0; width: 547px; height: 800px; background: var(--navy); }
  .back-frame { position: absolute; left: 16px; top: 16px; width: 511px; height: 768px; border: 1px solid var(--orange-soft); }
  .back-tagline { position: absolute; top: 40px; left: 0; width: 547px; text-align: center; font-size: 11.5px; letter-spacing: .4px; line-height: 15px; }
  .back-tagline .rule { display: inline-block; width: 28px; height: 1px; background: var(--orange); vertical-align: middle; margin: 0 8px; }
  .back-title { position: absolute; top: 78px; left: 0; width: 547px; text-align: center; font-family: "Oswald", sans-serif; font-weight: 600; font-size: 54px; line-height: 60px; letter-spacing: .5px; }
  .accent { color: var(--orange); }
  .divider { position: absolute; height: 12px; display: flex; align-items: center; justify-content: center; gap: 10px; }
  .divider span { height: 1px; background: var(--orange); flex: 1; }
  .divider i { width: 8px; height: 8px; border: 1.5px solid var(--orange); border-radius: 50%; }
  .back-divider { top: 147px; left: 140px; width: 290px; }
  .back-body { position: absolute; top: 168px; left: 47px; width: 458px; font-size: 11px; line-height: 14px; }
  .back-body h3 { color: var(--orange); font-weight: 400; font-size: 12px; margin-bottom: 3px; }
  .back-body p { margin-bottom: 8px; }
  .back-body ul { list-style: none; margin: 2px 0 8px 30px; }
  .back-body li { line-height: 16.6px; position: relative; }
  .back-body li::before { content: ""; position: absolute; left: -14px; top: 7px; width: 4px; height: 4px; border-radius: 50%; background: var(--orange); }
  .back-body .series { font-style: italic; }
  .back-ornament { position: absolute; top: 704px; left: 75px; width: 210px; }
  .barcode-box { position: absolute; left: 335px; top: 669px; width: 170px; height: 106px; background: var(--cream); border-radius: 2px; }

  /* ---------- spine ---------- */
  .spine { position: absolute; left: 547px; top: 0; width: 105px; height: 800px; background: var(--navy-deep); border-left: 1px solid #1f2f4a; border-right: 1px solid #1f2f4a; }
  .spine-rule { position: absolute; left: 40px; width: 25px; height: 1px; background: var(--orange); }
  .spine-title, .spine-author { position: absolute; left: 52px; writing-mode: vertical-rl; font-family: "Oswald", sans-serif; font-weight: 700; transform: translateX(-50%); white-space: nowrap; }
  .spine-title { top: 50px; font-size: 37px; letter-spacing: 1px; }
  .spine-author { top: 410px; font-size: 20px; letter-spacing: 1px; }
  .spine-mark { position: absolute; left: 45px; width: 14px; height: 14px; border: 2px solid var(--orange); border-radius: 50%; }
  .spine-wheel { position: absolute; left: 34px; top: 717px; width: 36px; height: 36px; border: 3px solid var(--orange); border-radius: 50%; }

  /* ---------- front cover ---------- */
  .front { position: absolute; left: 652px; top: 0; width: 548px; height: 800px; overflow: hidden; }
  .front-scene { position: absolute; inset: 0; background:
      radial-gradient(ellipse 45% 22% at 18% 66%, rgba(236,214,170,.85), transparent 80%),
      radial-gradient(ellipse 40% 26% at 72% 46%, rgba(255,190,80,.95), rgba(242,160,50,.45) 50%, transparent 80%),
      linear-gradient(180deg, #4d6d96 0%, #8ea3bb 22%, #c8cfd2 36%, #e7c897 46%, #d9b07a 54%, #b8a68c 62%, #6f7480 76%, #22324c 88%, var(--navy-deep) 100%); }
  .front-frame { position: absolute; left: 18px; top: 14px; width: 512px; height: 771px; border: 1px solid var(--orange-soft); }
  .front-tagline { position: absolute; top: 32px; width: 548px; text-align: center; font-family: "Oswald", sans-serif; font-weight: 500; font-size: 16px; line-height: 19px; color: var(--navy-deep); letter-spacing: .3px; }
  .front-tagline .rule { display: inline-block; width: 34px; height: 2px; background: var(--orange); vertical-align: middle; margin: 0 8px; }
  .title-before, .title-pay { position: absolute; left: 0; width: 548px; text-align: center; font-family: "Archivo Black", sans-serif; transform-origin: center top; }
  .title-before { top: 58px; font-size: 100px; line-height: 100px; color: var(--ink); transform: scaleY(1.3); letter-spacing: -1px; }
  .title-you { position: absolute; top: 176px; left: 60px; width: 428px; display: flex; align-items: center; gap: 12px; font-family: "Archivo Black", sans-serif; font-size: 34px; line-height: 34px; color: var(--ink); }
  .title-you span { flex: 1; height: 4px; background: var(--ink); }
  .title-pay { top: 200px; font-size: 112px; line-height: 112px; color: var(--orange); transform: scaleY(1.12); letter-spacing: 2px; }
  .front-divider { top: 314px; left: 130px; width: 170px; }
  .front-divider span { background: var(--navy-deep); }
  .front-divider i { border-color: var(--navy-deep); }
  .subtitle { position: absolute; top: 336px; left: 60px; width: 260px; text-align: center; font-family: "Oswald", sans-serif; font-weight: 600; font-size: 17px; line-height: 20px; color: var(--navy-deep); }
  .subtitle .accent { color: var(--orange-strong); }
  .features { position: absolute; top: 418px; left: 35px; list-style: none; }
  .feature { display: flex; align-items: center; height: 48px; }
  .feature-icon { flex: none; width: 36px; height: 36px; border-radius: 50%; background: var(--navy-deep); display: flex; align-items: center; justify-content: center; margin-right: 13px; }
  .feature-text { font-family: "Oswald", sans-serif; font-weight: 600; font-size: 11.5px; line-height: 13px; color: var(--navy-deep); width: 100px; }
  .badge { position: absolute; left: 371px; top: 549px; width: 120px; height: 120px; border-radius: 50%; background: rgba(10,22,40,.92); border: 2px solid var(--orange); text-align: center; font-family: "Oswald", sans-serif; font-weight: 500; font-size: 13px; line-height: 16px; padding-top: 28px; }
  .badge-text { display: block; }
  .front-wheel { position: absolute; left: 243px; top: 640px; width: 40px; height: 40px; border: 3px solid var(--orange); border-radius: 50%; }
  .author { position: absolute; top: 690px; left: 0; width: 548px; text-align: center; font-family: "Oswald", sans-serif; font-weight: 700; font-size: 38px; line-height: 48px; white-space: nowrap; }
  .credentials { position: absolute; top: 748px; left: 0; width: 548px; text-align: center; font-family: "Oswald", sans-serif; font-weight: 500; font-size: 14px; color: var(--orange); letter-spacing: .4px; }
  .credentials .rule { display: inline-block; width: 34px; height: 1px; background: var(--orange); vertical-align: middle; margin: 0 6px; }
</style>
</head>
<body>
<div class="cover">

  <section class="back">
    <div class="back-frame"></div>
    <div class="back-tagline"><span class="rule"></span>THE SMART BUYER’S GUIDE TO FINDING<span class="rule"></span><br>THE RIGHT BOAT AND BOATING WITH CONFIDENCE</div>
    <h1 class="back-title">BEFORE YOU <span class="accent">PAY</span></h1>
    <div class="divider back-divider"><span></span><i></i><span></span></div>
    <div class="back-body">
      <h3>Before You Pay:</h3>
      <p>Before you spend thousands on a boat… spend a few hours learning what experienced boaters wish they knew.</p>
      <p>Buying a recreational boat is exciting—but it can also be expensive, confusing, and full of costly mistakes.</p>
      <p>This practical guide helps first-time buyers understand how to evaluate boats, compare ownership options, recognize hidden costs, and avoid expensive surprises before signing the paperwork. Through easy-to-follow explanations, checklists, comparison tables, and illustrations, you’ll gain the confidence to make informed decisions and purchase a boat that truly fits your lifestyle.</p>
      <p>Whether you’re shopping for your first boat or upgrading to your next one, this book will help you buy smarter and avoid the mistakes that many owners only discover after it’s too late.</p>
      <h3>You’ll Learn How To:</h3>
      <ul>
        <li>Choose the right boat</li>
        <li>Compare ownership options</li>
        <li>Inspect boats with confidence</li>
        <li>Understand engines and systems</li>
        <li>Estimate ownership costs</li>
        <li>Avoid common buying mistakes</li>
        <li>Know when to hire a surveyor</li>
        <li>Negotiate from an informed position</li>
      </ul>
      <h3>About the Author</h3>
      <p>Captain Dorian K. Halvett is a U.S. Coast Guard Licensed Captain, certified boating instructor, military veteran, and experienced recreational boater. Having trained thousands of students and delivered hundreds of vessels, he created the Before You… series to help new boaters avoid costly mistakes and enjoy safer, more rewarding time on the water.</p>
      <h3>Series Tagline</h3>
      <p><span class="series">The Before You… Series</span><br>Helping new recreational boaters make smarter decisions before buying, boating, and traveling.</p>
    </div>
    <div class="divider back-ornament"><span></span><i style="width:34px;height:34px;border-width:3px"></i><span></span></div>
    <div class="barcode-box"></div>
  </section>

  <section class="spine">
    <div class="spine-rule" style="top:27px"></div>
    <div class="spine-title">BEFORE YOU <span class="accent">PAY</span></div>
    <div class="spine-mark" style="top:372px"></div>
    <div class="spine-author">CAPTAIN DORIAN K. HALVETT</div>
    <div class="spine-wheel"></div>
    <div class="spine-rule" style="top:780px"></div>
  </section>

  <section class="front">
    <div class="front-scene" role="img" aria-label="Photograph of a white bowrider boat cruising across open water at sunset beneath a cable-stayed bridge"></div>
    <div class="front-frame"></div>
    <div class="front-tagline"><span class="rule"></span>THE SMART BUYER’S GUIDE TO FINDING<span class="rule"></span><br>THE RIGHT BOAT AND BOATING WITH CONFIDENCE</div>
    <div class="title-before">BEFORE</div>
    <div class="title-you"><span></span>YOU<span></span></div>
    <div class="title-pay">PAY</div>
    <div class="divider front-divider"><span></span><i></i><span></span></div>
    <p class="subtitle">A COMPLETE GUIDE FOR<br><span class="accent">FIRST-TIME BOAT BUYERS</span><br>— FROM SHOPPING TO SEA TRIAL<br>AND BEYOND</p>
    <ul class="features">
      <li class="feature"><span class="feature-icon"><svg width="20" height="20" viewBox="0 0 20 20" fill="none" stroke="#fff" stroke-width="2"><circle cx="8" cy="8" r="5.5"/><path d="M12 12l6 6"/></svg></span><span class="feature-text">FIND THE RIGHT BOAT FOR YOUR NEEDS AND BUDGET</span></li>
      <li class="feature"><span class="feature-icon"><svg width="20" height="20" viewBox="0 0 20 20" fill="none" stroke="#fff" stroke-width="2"><rect x="2" y="3" width="14" height="14"/><path d="M5 10l3 3 8-9"/></svg></span><span class="feature-text">SHOP SMART AND AVOID RED FLAGS</span></li>
      <li class="feature"><span class="feature-icon"><svg width="20" height="20" viewBox="0 0 20 20" fill="#fff"><path d="M2 12h16l-3 4H5z"/><rect x="7" y="7" width="6" height="4"/><path d="M2 18q2-1.5 4 0t4 0 4 0 4 0" stroke="#fff" fill="none" stroke-width="1.2"/></svg></span><span class="feature-text">SEA TRIAL<br>LIKE A PRO</span></li>
      <li class="feature"><span class="feature-icon"><svg width="20" height="20" viewBox="0 0 20 20" fill="none" stroke="#fff" stroke-width="1.8"><rect x="4" y="3" width="12" height="15" rx="1"/><path d="M7 7h6M7 10.5h6M7 14h6"/></svg></span><span class="feature-text">INSPECTIONS, SURVEYS &amp; NEGOTIATIONS</span></li>
      <li class="feature"><span class="feature-icon"><svg width="20" height="20" viewBox="0 0 20 20"><text x="10" y="16" text-anchor="middle" fill="#fff" font-family="Oswald, sans-serif" font-weight="700" font-size="18">$</text></svg></span><span class="feature-text">UNDERSTAND TRUE OWNERSHIP COSTS</span></li>
    </ul>
    <div class="badge"><span class="badge-text">AVOID COSTLY<br>MISTAKES.<br>BUY WITH<br><span class="accent">CONFIDENCE.</span></span></div>
    <div class="front-wheel"></div>
    <div class="author">CAPTAIN DORIAN K. HALVETT</div>
    <div class="credentials"><span class="rule"></span>USCG LICENSED CAPTAIN ★ CERTIFIED INSTRUCTOR ★ VETERAN<span class="rule"></span></div>
  </section>

</div>
</body>
</html>
```